PowerPoint Template

We would like new powerpoint template for our organization: Fjordvik Data Guild.
Enclosed you find our logo and old template.
Industry/Entity Type
Computer
Requirements
Must have
- 1. Logo
2. Footer (for autor)
3. Font: Variations of ARIAL

```html
<!DOCTYPE html>
<html lang="no">
<head>
<meta charset="utf-8">
<title>Fjordvik Data Guild – PowerPoint Template</title>
<link rel="stylesheet" href="https://fonts.googleapis.com/css2?family=Arimo:wght@400;700&display=swap">
<style>
  :root {
    --page-bg: #e4f0fa;
    --slide-light: #d6ecfb;
    --slide-mid: #8cc8ef;
    --slide-deep: #4fa6df;
    --title-ink: #1a5e8a;
    --body-ink: #1f6fa3;
    --footer-ink: #1c84c6;
    --teal: #2aa7c9;
    --brand-mark: #e8394a;
    --white: #ffffff;
  }
  * { box-sizing: border-box; margin: 0; padding: 0; }
  html, body {
    width: 1200px; height: 1000px; overflow: hidden;
    background: radial-gradient(ellipse at center, #f6fbff 0%, var(--page-bg) 70%, #cfe4f5 100%);
    font-family: "Arimo", Arial, sans-serif;
  }
  .canvas { position: relative; width: 1200px; height: 1000px; }
  .slide {
    position: absolute; width: 557px; height: 417px; overflow: hidden;
    box-shadow: 0 0 18px rgba(255,255,255,0.9);
  }
  .slide--title   { left: 20px;  top: 60px; }
  .slide--content-a { left: 623px; top: 60px; }
  .slide--content-b { left: 20px;  top: 522px; }
  .slide--content-c { left: 623px; top: 522px; }

  .backdrop {
    position: absolute; inset: 0;
    background:
      radial-gradient(ellipse 55% 60% at 55% 40%, rgba(255,255,255,0.75) 0%, rgba(255,255,255,0) 70%),
      linear-gradient(160deg, var(--slide-mid) 0%, var(--slide-light) 45%, var(--slide-mid) 80%, var(--slide-deep) 100%);
  }
  .slide--title .backdrop {
    background:
      radial-gradient(ellipse 50% 55% at 50% 45%, rgba(255,255,255,0.55) 0%, rgba(255,255,255,0) 70%),
      linear-gradient(150deg, var(--slide-deep) 0%, var(--slide-mid) 40%, #a9d7f4 70%, var(--slide-mid) 100%);
  }
  .bands { position: absolute; inset: 0; width: 557px; height: 417px; }

  .slide-title {
    position: absolute; left: 40px; top: 44px;
    font-weight: 700; font-size: 30px; color: var(--title-ink); letter-spacing: 0.3px;
  }
  .slide--content-a .slide-title, .slide--content-c .slide-title { left: 40px; }
  .bullets {
    position: absolute; left: 116px; top: 116px; width: 320px;
    list-style: none; font-size: 19px; line-height: 26px; color: var(--body-ink);
  }
  .bullets li { position: relative; padding-left: 24px; margin-bottom: 5px; }
  .bullets li::before {
    content: ""; position: absolute; left: 0; top: 10px;
    width: 7px; height: 7px; background: var(--body-ink);
  }
  .footer-credit {
    position: absolute; left: 16px; top: 379px;
    font-size: 11px; font-weight: 700; color: var(--footer-ink); letter-spacing: 0.2px;
  }
  .brand {
    position: absolute; display: flex; align-items: center;
    font-weight: 700; color: var(--title-ink);
  }
  .brand__square { background: var(--brand-mark); flex: none; }
  .brand--footer { right: 14px; bottom: 14px; width: 92px; gap: 6px; font-size: 11px; line-height: 12px; }
  .brand--footer .brand__square { width: 14px; height: 14px; }
  .brand--hero { left: 200px; top: 140px; width: 190px; gap: 12px; font-size: 26px; line-height: 29px; flex-wrap: nowrap; }
  .brand--hero .brand__square { width: 40px; height: 40px; }
  .brand-url {
    position: absolute; left: 205px; top: 270px; font-size: 17px; color: var(--title-ink);
  }
  .title-slide-heading {
    position: absolute; left: 34px; top: 352px;
    font-weight: 700; font-size: 27px; color: var(--title-ink); letter-spacing: 0.5px;
  }
</style>
</head>
<body>
<main class="canvas">

  <section class="slide slide--title">
    <div class="backdrop" role="img" aria-label="Soft blue abstract background of interlaced arcs"></div>
    <svg class="bands" viewBox="0 0 557 417" aria-hidden="true">
      <path d="M0 372 C160 330 380 300 557 150" fill="none" stroke="#fff" stroke-opacity="0.55" stroke-width="22"/>
      <path d="M0 345 C170 320 400 280 557 185" fill="none" stroke="#fff" stroke-opacity="0.4" stroke-width="6"/>
      <path d="M0 400 C190 350 420 320 557 215" fill="none" stroke="#fff" stroke-opacity="0.35" stroke-width="10"/>
    </svg>
    <div class="brand brand--hero"><span class="brand__square"></span><span>Fjordvik Data Guild</span></div>
    <div class="brand-url">fjordvikdata.no</div>
    <h1 class="title-slide-heading">TITLE SLIDE</h1>
  </section>

  <section class="slide slide--content-a">
    <div class="backdrop" role="img" aria-label="Soft blue abstract background of interlaced arcs"></div>
    <svg class="bands" viewBox="0 0 557 417" aria-hidden="true">
      <defs>
        <linearGradient id="stripeA" x1="0" x2="1"><stop offset="0" stop-color="#fff"/><stop offset="1" stop-color="#fff" stop-opacity="0.2"/></linearGradient>
      </defs>
      <path d="M0 342 Q280 356 557 390 L557 417 L0 417 Z" fill="#bfe2f8" fill-opacity="0.7"/>
      <path d="M0 340 Q280 352 557 378 L557 392 Q280 368 0 362 Z" fill="url(#stripeA)"/>
      <path d="M557 235 Q522 330 480 417 L557 417 Z" fill="var(--teal)"/>
    </svg>
    <h2 class="slide-title">Hva gjør vi?</h2>
    <ul class="bullets">
      <li>Markedsfører arrangementer</li>
      <li>Bidrar til å verve medlemmer</li>
      <li>Skaper synlighet i Sosiale Medier</li>
      <li>Bygger merkevare og FDGs omdømme</li>
    </ul>
    <p class="footer-credit">PRESENTATION BY:</p>
    <div class="brand brand--footer"><span class="brand__square"></span><span>Fjordvik Data Guild</span></div>
  </section>

  <section class="slide slide--content-b">
    <div class="backdrop" role="img" aria-label="Soft blue abstract background of interlaced arcs"></div>
    <svg class="bands" viewBox="0 0 557 417" aria-hidden="true">
      <defs>
        <linearGradient id="stripeB" x1="0" x2="1"><stop offset="0" stop-color="#fff"/><stop offset="1" stop-color="#fff" stop-opacity="0.2"/></linearGradient>
      </defs>
      <path d="M0 342 Q280 356 557 390 L557 417 L0 417 Z" fill="#bfe2f8" fill-opacity="0.7"/>
      <path d="M0 340 Q280 352 557 378 L557 392 Q280 368 0 362 Z" fill="url(#stripeB)"/>
      <path d="M557 235 Q522 330 480 417 L557 417 Z" fill="var(--teal)"/>
    </svg>
    <h2 class="slide-title">Hva gjør vi?</h2>
    <ul class="bullets">
      <li>Markedsfører arrangementer</li>
      <li>Bidrar til å verve medlemmer</li>
      <li>Skaper synlighet i Sosiale Medier</li>
      <li>Bygger merkevare og FDGs omdømme</li>
    </ul>
    <p class="footer-credit">PRESENTATION BY:</p>
    <div class="brand brand--footer"><span class="brand__square"></span><span>Fjordvik Data Guild</span></div>
  </section>

  <section class="slide slide--content-c">
    <div class="backdrop" role="img" aria-label="Soft blue abstract background of interlaced arcs"></div>
    <svg class="bands" viewBox="0 0 557 417" aria-hidden="true">
      <defs>
        <linearGradient id="stripeC" x1="0" x2="1"><stop offset="0" stop-color="#fff"/><stop offset="1" stop-color="#fff" stop-opacity="0.2"/></linearGradient>
      </defs>
      <path d="M0 342 Q280 356 557 390 L557 417 L0 417 Z" fill="#bfe2f8" fill-opacity="0.7"/>
      <path d="M0 340 Q280 352 557 378 L557 392 Q280 368 0 362 Z" fill="url(#stripeC)"/>
      <path d="M557 235 Q522 330 480 417 L557 417 Z" fill="var(--teal)"/>
    </svg>
    <h2 class="slide-title">Hva gjør vi?</h2>
    <ul class="bullets">
      <li>Markedsfører arrangementer</li>
      <li>Bidrar til å verve medlemmer</li>
      <li>Skaper synlighet i Sosiale Medier</li>
      <li>Bygger merkevare og FDGs omdømme</li>
    </ul>
    <p class="footer-credit">PRESENTATION BY:</p>
    <div class="brand brand--footer"><span class="brand__square"></span><span>Fjordvik Data Guild</span></div>
  </section>

</main>
</body>
</html>
```